Local Contractor needs Upscale Web Design

This website needs to have an upscale look with a very modern feel.

This is for a home page psd layout

Please build your psd file to match the look of this template: http://www.layoutorchard.example/demo/73815.html

Please change the color scheme to the colors of the attached logo

Add Logo that is attached.

Phone Number:
507-392-6184

Must Include these pages in a horizontal menu bar in this order:
Home, About, Services, Portfolio, Testimonials, Contact

For the rotating banners:
1. Construction - 35+ Years and Growing
2. Capabilities - Complete Line of Services
3. Commitment - Quality and Attention to Detail

Images under rotating banner:
Image 1, 2, 3 (Attached - Crop to fit)

What We're Thinking Section - Change title text to "Retail Space Construction" (Fill the remainder with latin text)

Who Are We Section - Change title text to "Industrial Construction" (Fill the remainder with latin text)

Project Gallery - Image 4, 5, 6, 7 (Attached - Crop to fit)

Remove the sections towards the bottom titled "Why Us" & "Services"

Please make the map show this address:
2917 88th St NW, Pine Hollow, MN 55318

Footer:
Quarry Ridge Construction © 2015 | Powered by Bright Pixel Works

```html
<!DOCTYPE html>
<html lang="en">
<head>
<meta charset="utf-8">
<title>Quarry Ridge Construction</title>
<link rel="stylesheet" href="https://fonts.googleapis.com/css2?family=Questrial&family=Mulish:ital,wght@0,400;0,700;1,400;1,700&display=swap">
<style>
:root{
  --maroon:#8e1b24;
  --maroon-dark:#7a141c;
  --maroon-soft:#b4545b;
  --frame:#c9737a;
  --text:#2b2b2b;
  --muted:#a7a7a7;
  --rule:#e6e6e6;
  --white:#ffffff;
  --map:#e9e7e2;
}
*{box-sizing:border-box;margin:0;padding:0}
html,body{width:1200px;height:2338px;overflow:hidden;background:var(--white)}
body{position:relative;font-family:"Questrial",sans-serif;color:var(--text)}
.abs{position:absolute}

/* hero */
.hero{left:0;top:0;width:1200px;height:584px;
  background:linear-gradient(180deg,#a5505a 0%,#93323b 45%,#7d1f28 100%)}
.hero-photo{left:0;top:0;width:1200px;height:584px;
  background:linear-gradient(90deg,rgba(120,30,38,.35),rgba(160,80,88,.15) 50%,rgba(110,25,34,.35))}
.phone{left:884px;top:12px;display:flex;align-items:center;gap:10px;color:var(--white);font-size:19px}
.brand{left:189px;top:70px;display:flex;align-items:center;gap:12px;color:var(--white);font-size:30px;letter-spacing:1px;line-height:1.05}
.brand-mark{width:26px;height:26px;background:var(--white)}
.nav{left:474px;top:147px;display:flex;gap:0;color:var(--white);font-size:17px}
.nav a{color:inherit;text-decoration:none;position:absolute;white-space:nowrap}
.nav .active{font-weight:700;border-bottom:2px solid var(--white);padding-bottom:2px}
.hero-title{left:181px;top:326px;color:var(--white);font-size:64px;font-weight:700;letter-spacing:1px;font-family:"Mulish",sans-serif}
.hero-sub{left:183px;top:405px;color:var(--white);font-size:20px}
.dots{left:188px;top:561px;display:flex;gap:4px}
.dot{width:16px;height:16px;border-radius:50%;border:2px solid var(--white)}
.dot.on{background:var(--white)}

/* featured images */
.frame{border:2px solid var(--frame);padding:6px;background:var(--white)}
.ph{width:100%;height:100%}
.btn{border:2px solid var(--maroon);color:var(--maroon);font-size:16px;display:flex;align-items:center;justify-content:center;letter-spacing:.5px}

/* cards */
.card{border:2px solid var(--frame);padding:14px 12px}
.card-title{font-family:"Mulish",sans-serif;font-weight:700;font-style:italic;color:var(--maroon);font-size:25px;padding-bottom:14px;border-bottom:1px solid var(--rule)}
.card-lead{font-family:"Mulish",sans-serif;font-style:italic;font-size:22px;margin-top:18px;color:var(--text)}
.card-body{font-family:"Mulish",sans-serif;font-style:italic;font-size:14px;color:var(--muted);line-height:1.3;margin-top:12px}
.card .btn{position:absolute;left:14px;bottom:18px;width:148px;height:38px}

/* gallery */
.section-title{left:172px;top:1528px;font-family:"Mulish",sans-serif;font-weight:700;color:var(--maroon);font-size:23px;letter-spacing:1px}
.section-rule{left:172px;top:1564px;width:858px;height:1px;background:var(--rule)}
.next{left:939px;top:1525px;width:53px;height:38px;background:var(--maroon)}
.tile{width:426px;height:181px}
.view-more{left:600px;top:1586px;width:429px;height:181px;background:rgba(142,27,36,.72);color:var(--white);display:flex;align-items:center;justify-content:center;font-size:17px;letter-spacing:1px}

/* map + footer */
.map{left:0;top:2028px;width:1200px;height:238px;background:var(--map)}
.address{left:504px;top:2142px;font-size:18px;color:var(--maroon);line-height:1.3}
.footer{left:0;top:2266px;width:1200px;height:72px;background:var(--maroon)}
.footer-text{left:180px;top:2293px;color:var(--white);font-size:13px;font-family:"Mulish",sans-serif;font-weight:700}
.to-top{left:871px;top:2266px;width:156px;height:72px;background:#f4f4f4}
</style>
</head>
<body>

<header>
  <div class="abs hero"></div>
  <div class="abs hero-photo" role="img" aria-label="Storefront of a completed brick retail building under a maroon tint"></div>

  <div class="abs phone">
    <svg width="12" height="22" viewBox="0 0 12 22"><rect x="1" y="1" width="10" height="20" rx="2" fill="none" stroke="#fff" stroke-width="2"/><circle cx="6" cy="17" r="1.2" fill="#fff"/></svg>
    <span>507-392-6184</span>
  </div>

  <div class="abs brand"><span class="brand-mark"></span><span>QUARRY RIDGE<br>CONSTRUCTION</span></div>

  <nav class="abs nav">
    <a class="active" style="left:0">Home</a>
    <a style="left:81px">About</a>
    <a style="left:165px">Services</a>
    <a style="left:260px">Portfolio</a>
    <a style="left:354px">Testimonials</a>
    <a style="left:473px">Contact</a>
  </nav>

  <svg class="abs" style="left:10px;top:355px" width="16" height="36" viewBox="0 0 16 36"><path d="M14 2 2 18l12 16" fill="none" stroke="#fff" stroke-width="2.5" opacity=".8"/></svg>
  <svg class="abs" style="left:1174px;top:355px" width="16" height="36" viewBox="0 0 16 36"><path d="M2 2l12 16L2 34" fill="none" stroke="#fff" stroke-width="2.5" opacity=".8"/></svg>

  <h1 class="abs hero-title">CONSTRUCTION</h1>
  <p class="abs hero-sub">OF YOUR DREAMS</p>

  <div class="abs dots"><span class="dot on"></span><span class="dot"></span><span class="dot"></span></div>
</header>

<main>
  <div class="abs frame" style="left:162px;top:668px;width:568px;height:407px">
    <div class="ph" role="img" aria-label="Showroom with stone fireplace wall and freestanding tub" style="background:linear-gradient(135deg,#8a7a68,#c9c2b6 50%,#3d3a38)"></div>
  </div>
  <div class="abs frame" style="left:733px;top:668px;width:301px;height:205px">
    <div class="ph" role="img" aria-label="White kitchen with dark countertops" style="background:linear-gradient(135deg,#ddd9d3,#9c9790 60%,#4a4745)"></div>
  </div>
  <div class="abs frame" style="left:733px;top:877px;width:301px;height:198px">
    <div class="ph" role="img" aria-label="Bathroom with vessel sink and soaking tub" style="background:linear-gradient(135deg,#6a625a,#cfccc6 55%,#e9e7e3)"></div>
  </div>
  <div class="abs btn" style="left:164px;top:1089px;width:165px;height:35px">VIEW GALLERY</div>

  <article class="abs card" style="left:162px;top:1171px;width:436px;height:263px">
    <h2 class="card-title">RETAIL SPACE CONSTRUCTION</h2>
    <p class="card-lead">Lorem ipsum dolor sit amet</p>
    <p class="card-body">Lorem ipsum dolor sit amet, consectetuer adipiscing elit, sed diam nonummy nibh euismod tincidunt ut laoreet dolore magna aliquam erat volutpat.</p>
    <div class="btn">READ MORE</div>
  </article>
  <article class="abs card" style="left:635px;top:1171px;width:411px;height:263px">
    <h2 class="card-title">INDUSTRIAL CONSTRUCTION</h2>
    <p class="card-lead">Lorem ipsum dolor sit amet</p>
    <p class="card-body">Lorem ipsum dolor sit amet, consectetuer adipiscing elit, sed diam nonummy nibh euismod tincidunt ut laoreet dolore magna aliquam erat volutpat.</p>
    <div class="btn">READ MORE</div>
  </article>

  <h2 class="abs section-title">PROJECT GALLERY</h2>
  <div class="abs section-rule"></div>
  <div class="abs next"><svg width="53" height="38" viewBox="0 0 53 38"><path d="M24 14l5 5-5 5" fill="none" stroke="#fff" stroke-width="2"/></svg></div>

  <div class="abs tile" style="left:173px;top:1586px" role="img" aria-label="Kitchen with dark cabinetry and tiled backsplash" style="background:#5a4536"></div>
  <div class="abs tile" style="left:173px;top:1586px;background:linear-gradient(135deg,#6b4a2e,#c9a56e 45%,#3b2e27)" role="img" aria-label="Kitchen with dark cabinetry and tiled backsplash"></div>
  <div class="abs tile" style="left:603px;top:1586px;background:linear-gradient(135deg,#8a7a68,#c9c2b6)" role="img" aria-label="Showroom with stone fireplace wall"></div>
  <div class="abs view-more">VIEW MORE</div>
  <div class="abs tile" style="left:173px;top:1770px;background:linear-gradient(135deg,#e4e1dc,#9a958f 60%,#3e3b39)" role="img" aria-label="White kitchen with dark countertops"></div>
  <div class="abs tile" style="left:603px;top:1770px;background:linear-gradient(135deg,#5c554e,#d2cfc9 55%,#ecebe8)" role="img" aria-label="Bathroom with vessel sink and soaking tub"></div>

  <div class="abs map" role="img" aria-label="Street map around the office location"></div>
  <svg class="abs" style="left:586px;top:2078px" width="40" height="54" viewBox="0 0 40 54"><path d="M20 2C10 2 3 9 3 19c0 13 17 33 17 33s17-20 17-33C37 9 30 2 20 2z" fill="#8e1b24"/><circle cx="20" cy="19" r="7" fill="#fff"/></svg>
  <p class="abs address">2917 88th St NW, Pine<br>Hollow, MN 55318</p>
</main>

<footer>
  <div class="abs footer"></div>
  <p class="abs footer-text">Quarry Ridge Construction © 2015 &nbsp;|&nbsp; Powered by Bright Pixel Works</p>
  <div class="abs to-top"><svg width="156" height="72" viewBox="0 0 156 72"><path d="M66 40l12-11 12 11" fill="none" stroke="#555" stroke-width="2"/></svg></div>
</footer>

</body>
</html>
```